Lebens und Sozialberaterin  sucht Logo + Visitenkarten Design
Lebens und Sozialberaterin sucht Logo + Visitenkarten Design
Zielgruppe
Ich biete Beratungen in allen Lebenslagen an und bringe meine Klienten dazu neue Sichtweisen zu erlangen.
Lebenskrisen und Entscheidungssituationen
Beratung in psychosozialen Belastungssituationen
(Arbeitsverlust, Trennung, Mobbing, Alleinerziehung)
Beratung von Schul- und Berufslaufbahn
Erziehungsberatung
Konfliktmanagement (Beziehungsproblemen)
Paarberatung
Sexualberatung
Partnerschaft & Liebe
Mobbing
Stress & Burnout,....
Zielgruppe : Einzelpersonen , Paare, Familien, Firmen und Institutionen
Aufgabenstellung
Das Logo soll Vertrauen, Kompetenz und Wertschätzung kommunizieren. Es sollte einfach und verständlich sein und einen hohen Wiedererkennungswert haben . Ich denke, dass hier weniger oft mehr ist. Da ich in weiterer Folge auch Flyer benötige wäre es gut, wenn das Logo skallierbar wäre um es jeweils auch anzupassen. Farbtöne wie Türkis, Hellgrün, Blau,Gold und Pink gefallen mir sehr gut ich bin aber für jede weitere Farbvariation offen.
Beigefügt habe ich ein Beispiel, welches mir immer wieder gut gefällt, das Baumsymbol ist aber keine Voraussetzung da ich für alle anderen Ideen offen bin .
Visitenkarten können beidseitig bedruckt sein , eventuell vorne das LOGO und auf der Hinterseite meine Daten
Folgende Informationen für die Visitenkarte :
Systemische Lebens - und Sozialberatung
HandyNr. folgt noch !

```html
<!DOCTYPE html>
<html lang="de">
<head>
<meta charset="utf-8">
<title>Hanne Grut – Logo &amp; Visitenkarten</title>
<link rel="stylesheet" href="https://fonts.googleapis.com/css2?family=Red+Hat+Display:wght@500;700&family=Mulish:wght@400;500;600&display=swap">
<style>
  :root {
    --navy: #0d2a45;
    --gold: #c99a62;
    --gold-faint: #efe4d6;
    --paper: #ffffff;
    --card-edge: #e4e4e4;
  }
  * { margin: 0; padding: 0; box-sizing: border-box; }
  html, body { width: 1200px; height: 848px; overflow: hidden; background: var(--paper); }
  .sheet { position: relative; width: 1200px; height: 848px; font-family: "Mulish", sans-serif; }

  .brand-mark { position: absolute; border-radius: 50%; border: 5px solid var(--gold); }
  .brand-name { font-family: "Red Hat Display", sans-serif; font-weight: 700; letter-spacing: 0.08em; white-space: nowrap; }
  .brand-role { color: var(--gold); font-weight: 500; white-space: nowrap; }

  .logo-lockup { position: absolute; left: 0; top: 0; width: 1200px; height: 280px; }
  .logo-lockup .brand-mark { left: 523px; top: 36px; width: 154px; height: 154px; }
  .logo-lockup .brand-name { position: absolute; left: 0; width: 1200px; top: 202px; text-align: center; font-size: 40px; color: var(--navy); }
  .logo-lockup .brand-role { position: absolute; left: 0; width: 1200px; top: 246px; text-align: center; font-size: 13px; }

  .card { position: absolute; top: 316px; width: 399px; height: 255px; overflow: hidden; }
  .card-front { left: 177px; background: var(--navy); }
  .card-front .brand-mark { left: 150px; top: 69px; width: 102px; height: 102px; border-width: 4px; }
  .card-front .brand-name { position: absolute; left: 0; width: 399px; top: 176px; text-align: center; font-size: 26px; color: var(--paper); }
  .card-front .brand-role { position: absolute; left: 0; width: 399px; top: 211px; text-align: center; font-size: 11px; }

  .card-back { left: 611px; background: var(--paper); border: 1px solid var(--card-edge); }
  .card-back .backdrop-ring { position: absolute; left: 222px; top: 46px; width: 190px; height: 190px; border-radius: 50%; border: 9px solid var(--gold-faint); }
  .card-back .holder-name { position: absolute; left: 71px; top: 60px; font-family: "Red Hat Display", sans-serif; font-weight: 500; font-size: 19px; letter-spacing: 0.04em; color: var(--navy); }
  .card-back .brand-role { position: absolute; left: 101px; top: 87px; font-size: 9.5px; }

  .contact-list { position: absolute; left: 24px; top: 146px; list-style: none; }
  .contact-list li { display: flex; align-items: center; height: 20px; font-size: 11.5px; color: var(--navy); }
  .contact-list svg { width: 13px; height: 13px; margin-right: 6px; flex: none; }
  .address { position: absolute; left: 24px; top: 218px; font-size: 11px; color: var(--navy); }
</style>
</head>
<body>
<main class="sheet">

  <section class="logo-lockup">
    <div class="brand-mark"></div>
    <div class="brand-name">HANNE GRUT</div>
    <div class="brand-role">Dipl. Lebens- und Sozialberaterin</div>
  </section>

  <section class="card card-front">
    <div class="brand-mark"></div>
    <div class="brand-name">HANNE GRUT</div>
    <div class="brand-role">Dipl. Lebens- und Sozialberaterin</div>
  </section>

  <section class="card card-back">
    <div class="backdrop-ring"></div>
    <div class="holder-name">Hanne Grut</div>
    <div class="brand-role">Dipl. Lebens- und Sozialberaterin</div>

    <ul class="contact-list">
      <li>
        <svg viewBox="0 0 14 14" aria-hidden="true"><circle cx="7" cy="7" r="6.2" fill="none" stroke="#c99a62" stroke-width="1.2"/><path d="M4.6 3.8c.4-.3.8-.2 1 .2l.6 1.1c.2.3.1.6-.2.8l-.4.3c.4.9 1 1.5 1.9 1.9l.3-.4c.2-.3.5-.4.8-.2l1.1.6c.4.2.5.6.2 1-.5.7-1.2.9-2 .6-1.7-.7-2.9-1.9-3.6-3.6-.3-.8-.1-1.5.3-1.9z" fill="#c99a62"/></svg>
        +43 660 - 418 275 90
      </li>
      <li>
        <svg viewBox="0 0 14 14" aria-hidden="true"><circle cx="7" cy="7" r="6.2" fill="#c99a62"/><circle cx="7" cy="7" r="3.4" fill="none" stroke="#fff" stroke-width="0.9"/><path d="M3.6 7h6.8M7 3.6c-1.3 1.8-1.3 5 0 6.8M7 3.6c1.3 1.8 1.3 5 0 6.8" fill="none" stroke="#fff" stroke-width="0.8"/></svg>
        www.hanne-grut.at
      </li>
      <li>
        <svg viewBox="0 0 14 14" aria-hidden="true"><circle cx="7" cy="7" r="6.2" fill="#c99a62"/><rect x="3.8" y="4.8" width="6.4" height="4.6" rx="0.6" fill="none" stroke="#fff" stroke-width="0.9"/><path d="M3.9 5l3.1 2.4L10.1 5" fill="none" stroke="#fff" stroke-width="0.9"/></svg>
        beratung@hanne-grut.at
      </li>
    </ul>
    <div class="address">Lindengasse 48B • 1070 Wien</div>
  </section>

</main>
</body>
</html>
```